Ridgecrest Balusters Website Redesign

I want a fresh new design for my website. Original website
www.ridgecrestbalusters.example. Will need to add additional photos for winning designer. Please use the basic layout for new design. Looking to get a more modern, functional site to attract new customer and ne bale to highlight past projects. Need it to be easy to navigate and get in touch with me for inquiries.

Target Market(s)

Builders and home owners in WA state

Industry/Entity Type

Building, Construction, Deck building

Coding

Coded - Design and coding required

Number of Pages Required

5+ page

Font styles to use
Sans Serif

Colors
0054AA
0677BA
7BADD7
CADEEF
E8F1F8
0094D4
00A9DD
6FCCEA
C7EBF8
E9F6FB
00AB8E
00BBA5
67D7C9
C6EFE9
E9F9F6
59FF00
82FF00
B8FF75
E3FFCB
F4FFEA

Requirements
Must have
• Will need to add more photos of completed projects
Nice to have
• Fresh take on old website, something modern
Should not have
• Nothing comes to mind

```html
<!DOCTYPE html>
<html lang="en">
<head>
<meta charset="utf-8">
<title>Ridgecrest Balusters</title>
<link href="https://fonts.googleapis.com/css2?family=Montserrat:wght@400;500;600;700&family=Oswald:wght@600&display=swap" rel="stylesheet">
<style>
:root{
  --teal:#00AB8E;
  --teal-dark:#00977d;
  --mint:#E9F9F6;
  --mint-2:#C6EFE9;
  --ink:#1b1b1b;
  --text:#3a3a3a;
  --footer:#121212;
  --white:#ffffff;
}
*{margin:0;padding:0;box-sizing:border-box}
html,body{width:1200px;height:4812px;overflow:hidden}
body{font-family:'Montserrat',sans-serif;color:var(--text);background:var(--white);position:relative}
section,header,footer{position:absolute;left:0;width:1200px}
.abs{position:absolute}
.btn{position:absolute;background:var(--teal);color:var(--white);font-size:13px;display:flex;align-items:center;justify-content:center}
.label{color:var(--teal);font-size:11px;letter-spacing:.5px;text-transform:uppercase}
.h2{font-size:36px;font-weight:600;color:var(--ink)}
.center{left:0;width:1200px;text-align:center}

/* top bar */
.topbar{top:0;height:37px;background:var(--teal);color:var(--white);font-size:10px}
.topbar .item{position:absolute;top:12px;display:flex;align-items:center;gap:8px}
/* nav */
.nav{top:37px;height:75px;background:var(--mint)}
.brand{position:absolute;display:flex;align-items:center;gap:8px;font-weight:600;color:var(--teal-dark)}
.brand .mark{width:26px;height:26px;background:var(--teal-dark)}
.nav .menu a{position:absolute;top:29px;font-size:13px;color:var(--ink);text-decoration:none}
/* hero */
.hero{top:112px;height:525px;background:linear-gradient(160deg,#4a4e4c 0%,#2b2e2d 45%,#3c3a36 100%)}
.hero .eyebrow{top:145px;font-size:17px;color:var(--white);letter-spacing:.5px}
.hero .rule{top:155px;width:90px;height:1px;background:rgba(255,255,255,.6)}
.hero h1{top:190px;font-size:46px;font-weight:700;color:var(--white);line-height:68px}
/* about */
.about{top:637px;height:602px}
.photo{position:absolute}
.about p{position:absolute;left:640px;width:405px;font-size:12px;line-height:27px}
/* services */
.services{top:1239px;height:643px}
.services .band{position:absolute;top:0;left:0;width:1200px;height:340px;background:var(--mint)}
.card{position:absolute;top:172px;width:264px;height:337px;background:var(--mint)}
.card .img{height:224px}
.card h3{position:absolute;left:22px;top:246px;font-size:15px;font-weight:500;color:var(--teal)}
.card p{position:absolute;left:22px;top:275px;width:220px;font-size:10px;line-height:22px}
/* stats */
.stats{top:1882px;height:189px;background:var(--teal);color:var(--white)}
.stat{position:absolute;top:40px;width:220px;text-align:center}
.stat b{display:block;font-size:64px;font-weight:600;line-height:80px}
.stat span{font-size:12px}
/* intro */
.intro{top:2071px;height:731px}
.intro .copy{position:absolute;left:157px;top:218px;width:460px;font-size:12px;line-height:27px}
.intro .copy p{margin-bottom:15px}
.intro .copy strong{font-weight:600;color:var(--ink)}
/* process */
.process{top:2802px;height:480px;background:linear-gradient(180deg,#dff3ef 0%,var(--mint) 60%,#f3fbf9 100%)}
.step-num{position:absolute;top:190px;font-family:'Oswald',sans-serif;font-size:52px;font-weight:600;color:var(--teal)}
.step-img{position:absolute;top:203px;width:128px;height:128px;border-radius:50%}
.step-label{position:absolute;top:336px;width:200px;text-align:center;font-size:16px;font-weight:500;color:var(--ink);line-height:26px}
/* testimonials */
.testimonials{top:3282px;height:581px;background:var(--teal);color:var(--white)}
.testimonials h2{position:absolute;left:158px;top:212px;font-size:38px;font-weight:600}
.testimonials .lead{position:absolute;left:158px;top:275px;width:400px;font-size:12px;line-height:26px}
.quote{position:absolute;width:375px;height:120px;background:var(--white);border:6px solid #fff;outline:1px solid rgba(255,255,255,.6);outline-offset:4px;color:var(--text)}
.quote .avatar{position:absolute;left:14px;top:28px;width:62px;height:62px;border-radius:50%}
.quote p{position:absolute;left:96px;top:22px;width:260px;font-size:10px;line-height:21px}
.quote b{position:absolute;left:96px;top:76px;font-size:11px;font-weight:600;color:var(--ink)}
/* contact */
.contact{top:3863px;height:598px}
.contact .line{position:absolute;display:flex;gap:14px;align-items:center}
.contact .ico{width:34px;height:34px;border-radius:50%;background:var(--teal);display:flex;align-items:center;justify-content:center}
.contact .line small{display:block;font-size:9px}
.contact .line span{font-size:11px;font-weight:600;color:var(--ink)}
/* footer */
.footer{top:4461px;height:351px;background:var(--footer);color:#e6e6e6}
.fcol{position:absolute;top:44px;font-size:10px}
.fcol h4{font-size:12px;font-weight:600;color:var(--white);margin-bottom:12px}
.fcol li{list-style:none;line-height:30px}
.social{position:absolute;top:125px;width:26px;height:26px;border-radius:50%;background:#3a3a3a}
.copyright{position:absolute;left:0;width:1200px;top:325px;text-align:center;font-size:9px;color:#9a9a9a}
</style>
</head>
<body>

<header class="topbar">
  <div class="item" style="left:308px">
    <svg width="10" height="10" viewBox="0 0 24 24"><path fill="#fff" d="M6.6 10.8a15 15 0 006.6 6.6l2.2-2.2c.3-.3.7-.4 1-.2 1.1.4 2.3.6 3.6.6.6 0 1 .4 1 1V20c0 .6-.4 1-1 1A17 17 0 013 4c0-.6.4-1 1-1h3.5c.6 0 1 .4 1 1 0 1.3.2 2.5.6 3.6.1.3 0 .7-.2 1z"/></svg>
    (206) 555-0142</div>
  <div class="item" style="left:460px">
    <svg width="10" height="10" viewBox="0 0 24 24"><path fill="#fff" d="M2 5h20v14H2z"/><path fill="none" stroke="#00AB8E" stroke-width="2" d="M2 5l10 8 10-8"/></svg>
    info@ridgecrestbalusters.example</div>
  <div class="item" style="left:672px">
    <svg width="9" height="11" viewBox="0 0 24 30"><path fill="#fff" d="M12 0a10 10 0 00-10 10c0 8 10 20 10 20s10-12 10-20A10 10 0 0012 0zm0 14a4 4 0 110-8 4 4 0 010 8z"/></svg>
    4120 Orchard View Rd, Yakima, WA 98908</div>
</header>

<header class="nav">
  <div class="brand" style="left:160px;top:22px;font-size:15px"><span class="mark"></span>Ridgecrest Balusters</div>
  <nav class="menu">
    <a style="left:535px">Home</a>
    <a style="left:600px">Products</a>
    <a style="left:686px">About</a>
    <a style="left:752px">Railing Project Pictures</a>
    <a style="left:927px">Remodel Projects</a>
  </nav>
</header>

<section class="hero" role="img" aria-label="Balcony with aluminum and glass railings on a dark modern house">
  <div class="abs rule" style="left:378px"></div>
  <div class="abs rule" style="left:732px"></div>
  <div class="abs eyebrow center">RIDGECREST BALUSTERS</div>
  <h1 class="abs center">Aluminum Railings, Glass Railings,<br>Cable Railings &amp; Custom</h1>
  <div class="btn" style="left:518px;top:356px;width:164px;height:42px">Discover More</div>
</section>

<section class="about">
  <div class="photo" role="img" aria-label="Interior staircase with black metal railing" style="left:160px;top:111px;width:160px;height:372px;background:linear-gradient(180deg,#d9d7d2,#a6a29b)"></div>
  <div class="photo" role="img" aria-label="Multi-storey home with black balcony railings" style="left:338px;top:91px;width:262px;height:370px;background:linear-gradient(180deg,#bfc3c4,#8f8d83 60%,#5f6b60)"></div>
  <div class="abs" style="left:275px;top:131px;width:215px;height:380px;border:1.5px solid var(--teal)"></div>
  <div class="abs label" style="left:640px;top:88px">Licensed, Insured, &amp; Bonded</div>
  <div class="abs" style="left:640px;top:120px;font-size:38px;font-weight:600;color:var(--ink);line-height:55px">WA GC LICENSE<br># RIDGEBC804NS</div>
  <p style="top:235px"><strong style="font-weight:600;color:var(--ink)">Formed in 2020.</strong> At Ridgecrest Balusters, we believe that every outdoor space deserves the perfect blend of style, safety, and durability. Serving homeowners, builders &amp; commercial developers across the Washington State, we specialize in crafting custom railing systems designed to withstand the region's unique climate while enhancing the beauty of your outdoor living spaces.</p>
  <div class="btn" style="left:640px;top:418px;width:115px;height:38px">See More</div>
</section>

<section class="services">
  <div class="band"></div>
  <div class="abs label center" style="top:55px">What We're Offering</div>
  <div class="abs h2 center" style="top:78px">Services We're Providing You</div>
  <div class="card" style="left:178px"><div class="img" role="img" aria-label="Black vertical picket railing on a patio" style="background:linear-gradient(180deg,#8b7f70,#4d4a44)"></div><h3>Traditional Vertical Picket</h3><p>Lorem Ipsum is simply dummy text of the printing and typesetting industry.</p></div>
  <div class="card" style="left:468px"><div class="img" role="img" aria-label="Deck with topless glass railing overlooking trees" style="background:linear-gradient(180deg,#5d89c2,#9a7a55 70%,#7a4d2d)"></div><h3>Topless Glass</h3><p>Lorem Ipsum is simply dummy text of the printing and typesetting industry.</p></div>
  <div class="card" style="left:758px"><div class="img" role="img" aria-label="Balcony with framed glass railing" style="background:linear-gradient(180deg,#8d8f8c,#555956)"></div><h3>Framed Glass</h3><p>Lorem Ipsum is simply dummy text of the printing and typesetting industry.</p></div>
  <svg class="abs" style="left:568px;top:539px" width="64" height="16" viewBox="0 0 64 16">
    <path d="M14 8H2M6 4L2 8l4 4" stroke="#bbb" stroke-width="1.5" fill="none"/>
    <line x1="32" y1="2" x2="32" y2="14" stroke="#ccc"/>
    <path d="M50 8h12M58 4l4 4-4 4" stroke="#00AB8E" stroke-width="1.5" fill="none"/>
  </svg>
</section>

<section class="stats">
  <div class="stat" style="left:118px"><b>4+</b><span>Years of experience</span></div>
  <div class="stat" style="left:343px"><b>350</b><span>Happy clients</span></div>
  <div class="stat" style="left:565px"><b>16+</b><span>Business partners</span></div>
  <div class="stat" style="left:816px"><b>200+</b><span>Projects done</span></div>
</section>

<section class="intro">
  <div class="abs label center" style="top:94px">About Us</div>
  <div class="abs h2 center" style="top:113px">Our Introduction</div>
  <div class="copy">
    <p><strong>Why Choose Ridgecrest Balusters ?</strong></p>
    <p><strong>Locally Crafted, Regionally Resilient:</strong> Our railings are designed with the Pacific Northwest's weather in mind—rain, snow, and everything in between. We use durable materials that are resistant to corrosion, moisture, and the elements, ensuring your railings stand the test of time.</p>
    <p><strong>Custom Solutions for Every Need:</strong> We work closely with you to design and fabricate custom railing systems that perfectly suit your space, style, and functional requirements. From intricate designs to minimalistic finishes, we tailor every project to your vision.</p>
    <p><strong>Expert Installation &amp; Craftsmanship:</strong> Our skilled craftsmen take pride in delivering exceptional workmanship, while our professional installers ensure every railing is securely mounted and aligned to local safety codes.</p>
  </div>
  <div class="btn" style="left:157px;top:604px;width:115px;height:38px">See More</div>
  <div class="abs" role="img" aria-label="Grey modern building with black stair railing" style="left:662px;top:214px;width:380px;height:380px;border-radius:50%;background:linear-gradient(160deg,#9aa0a4,#6d706f 55%,#4f5150)"></div>
  <div class="abs" style="left:925px;top:465px;width:120px;height:120px;border-radius:50%;border:1.5px solid var(--teal)"></div>
</section>

<section class="process" role="presentation">
  <div class="abs h2 center" style="top:95px">Our Process</div>
  <div class="step-num" style="left:180px">01</div>
  <div class="step-img" role="img" aria-label="Outdoor staircase with black railing" style="left:210px;background:linear-gradient(160deg,#7b8a8e,#484d4c)"></div>
  <div class="step-label" style="left:172px">Consultation<br>&amp; Design</div>
  <div class="step-num" style="left:518px">02</div>
  <div class="step-img" role="img" aria-label="Installed exterior stair railing" style="left:548px;background:linear-gradient(160deg,#a0a3a2,#5c5f5e)"></div>
  <div class="step-label" style="left:512px">Professional<br>Installation</div>
  <div class="step-num" style="left:857px">03</div>
  <div class="step-img" role="img" aria-label="Multi-level deck with railings" style="left:886px;background:linear-gradient(160deg,#6a6e70,#3b3d3c)"></div>
  <div class="step-label" style="left:850px">Ongoing<br>Support</div>
  <svg class="abs" style="left:362px;top:240px" width="140" height="40" viewBox="0 0 140 40"><path d="M2 30C40 42 90 36 130 10" stroke="#00AB8E" fill="none" stroke-width="1.2"/><path d="M122 8l9 1-4 8" stroke="#00AB8E" fill="none" stroke-width="1.2"/></svg>
  <svg class="abs" style="left:705px;top:235px" width="140" height="40" viewBox="0 0 140 40"><path d="M2 28C40 2 95 4 130 24" stroke="#00AB8E" fill="none" stroke-width="1.2"/><path d="M121 26l9-1-4-8" stroke="#00AB8E" fill="none" stroke-width="1.2"/></svg>
</section>

<section class="testimonials">
  <svg class="abs" style="left:158px;top:90px" width="66" height="54" viewBox="0 0 66 54"><path fill="#3fc4ad" d="M0 0h28v28L16 54H4l10-26H0zM36 0h28v28L52 54H40l10-26H36z"/></svg>
  <div class="abs" style="left:158px;top:186px;font-size:11px">TESTIMONIALS</div>
  <h2>What Our Client Say</h2>
  <p class="lead">Lorem Ipsum is simply dummy text of the printing and typesetting industry. Lorem Ipsum has been the industry's standard dummy text ever since the 1500s, when an unknown printer took a galley of type and scrambled it to make a type specimen book.</p>
  <div class="quote" style="left:667px;top:91px"><div class="avatar" role="img" aria-label="Client portrait" style="background:#d9b98a"></div><p>Lorem Ipsum is dummy text of typesetting industry. Lorem Ipsum has been the industry's</p><b>- Mara Lindqvist</b></div>
  <div class="quote" style="left:615px;top:230px"><div class="avatar" role="img" aria-label="Client portrait" style="background:#8d8c88"></div><p>Lorem Ipsum is dummy text of typesetting industry. Lorem Ipsum has been the industry's</p><b>- Owen Pratt</b></div>
  <div class="quote" style="left:667px;top:371px"><div class="avatar" role="img" aria-label="Client portrait" style="background:#c9a99a"></div><p>Lorem Ipsum is dummy text of typesetting industry. Lorem Ipsum has been the industry's</p><b>- Jenna Hollis</b></div>
</section>

<section class="contact">
  <div class="abs h2" style="left:155px;top:77px">Need help? Get in touch</div>
  <p class="abs" style="left:157px;top:140px;width:460px;font-size:12px;line-height:26px">Lorem Ipsum is simply dummy text of the printing and typesetting industry. Lorem Ipsum has been the industry's standard dummy text.</p>
  <div class="line" style="left:838px;top:80px"><div class="ico"><svg width="14" height="14" viewBox="0 0 24 24"><path fill="#fff" d="M6.6 10.8a15 15 0 006.6 6.6l2.2-2.2c.3-.3.7-.4 1-.2 1.1.4 2.3.6 3.6.6.6 0 1 .4 1 1V20c0 .6-.4 1-1 1A17 17 0 013 4c0-.6.4-1 1-1h3.5c.6 0 1 .4 1 1 0 1.3.2 2.5.6 3.6.1.3 0 .7-.2 1z"/></svg></div><div><small>Call Us Now!</small><span>(206) 555-0142</span></div></div>
  <div class="line" style="left:838px;top:140px"><div class="ico"><svg width="14" height="12" viewBox="0 0 24 20"><path fill="#fff" d="M1 2h22v16H1z"/><path fill="none" stroke="#00AB8E" stroke-width="2" d="M1 2l11 8 11-8"/></svg></div><div><small>Email Us Now!</small><span>info@ridgecrestbalusters.example</span></div></div>
  <div class="abs" role="img" aria-label="Street map of the Yakima business location" style="left:157px;top:237px;width:886px;height:285px;background:linear-gradient(135deg,#eef0f2,#e3e6ea)"></div>
</section>

<footer class="footer">
  <div class="brand" style="left:160px;top:45px;font-size:15px;color:var(--teal)"><span class="mark" style="background:var(--teal)"></span>Ridgecrest Balusters</div>
  <div class="social" style="left:159px"></div>
  <div class="social" style="left:192px"></div>
  <div class="social" style="left:225px"></div>
  <div class="social" style="left:258px"></div>
  <div class="fcol" style="left:447px"><h4>OUR PRODUCTS</h4><ul><li>Traditional Vertical Picket</li><li>Topless Glass</li><li>Framed Glass</li><li>Cable Railing</li><li>Horizontal Railing</li><li>Custom Options</li><li>Glass Railing Stand Off Pins</li></ul></div>
  <div class="fcol" style="left:680px"><h4>SERVICES</h4><ul><li>About Us</li><li>Homeowners</li><li>Builders</li><li>Commercial Developers</li></ul></div>
  <div class="fcol" style="left:914px"><h4>RESOURCES</h4><ul><li>About Us</li><li>Request a quote</li><li>Contact Us</li></ul></div>
  <div class="abs" style="left:157px;top:310px;width:886px;height:1px;background:#2c2c2c"></div>
  <div class="copyright">Copyright © 2024. All rights reserved.</div>
</footer>

</body>
</html>
```